Business Card Trio Design

We need a set of business cards that all match but are not identical. We need one generic for the business and one for each of the two owners. We would like the cards to be similar to each other, but not identical. We have a logo and the colors of the logo are painstakingly chosen so if blue or green is used, we prefer our specific blue and green. Our logo pops better on a black background as well. We are open to double-sided, but it is not the top choice. We would love some either gold or silver accents that are in a foiled appearance. We sell uniforms (scrubs, culinary, EMT, police, fire, business, all types except kids and sports), shoes, equipment, and accessories. We also have facebook, pinterest, instagram, and twitter that we would like to have them follow and we offer splitwell in the store we would like the card to also advertise.

```html
<!DOCTYPE html>
<html lang="en">
<head>
<meta charset="UTF-8">
<title>Jadeline Apparel — Business Cards</title>
<link href="https://fonts.googleapis.com/css2?family=Montserrat:wght@400;500;700&display=swap" rel="stylesheet">
<style>
  :root {
    --brand-green: #0f9470;
    --brand-blue: #86a6c6;
    --ink: #3a3a3a;
    --card-white: #ffffff;
    --card-black: #2b2b2b;
    --backdrop: #4a4a4a;
  }
  * { box-sizing: border-box; margin: 0; padding: 0; }
  html, body {
    width: 1200px; height: 1200px; overflow: hidden;
    background: var(--backdrop);
    font-family: 'Montserrat', sans-serif;
  }
  .sheet {
    width: 1200px; height: 1200px;
    display: flex; flex-direction: column; align-items: center; justify-content: center;
    gap: 60px;
  }
  .card {
    position: relative;
    width: 840px; height: 480px;
    border-radius: 36px;
    overflow: hidden;
    box-shadow: 0 18px 40px rgba(0,0,0,0.45);
  }
  /* Front */
  .card-front { background: var(--card-white); }
  .identity {
    position: absolute; left: 70px; top: 120px;
    padding-left: 22px;
    border-left: 8px solid var(--brand-green);
  }
  .identity .name {
    font-weight: 700; font-size: 46px; line-height: 1;
    color: var(--brand-green); letter-spacing: 0.5px;
  }
  .identity .role {
    margin-top: 6px; font-size: 22px; font-weight: 500; color: var(--ink);
  }
  .contacts {
    position: absolute; left: 100px; top: 262px;
    list-style: none;
  }
  .contacts li {
    display: flex; align-items: center; gap: 14px;
    font-size: 19px; color: var(--ink); height: 34px;
  }
  .contacts svg { width: 22px; height: 22px; flex: none; }
  .contacts .social-box {
    width: 22px; height: 22px; border: 2.5px solid var(--brand-green); border-radius: 5px; flex: none;
  }
  .brand-lockup {
    position: absolute; right: 80px; top: 120px;
    display: flex; flex-direction: column; align-items: center; gap: 22px;
  }
  .brand-mark {
    width: 110px; height: 110px; border-radius: 50%;
    background: var(--brand-green);
  }
  .brand-name {
    font-weight: 500; font-size: 30px; letter-spacing: 4px;
    color: var(--brand-green); text-align: center; line-height: 1.2;
  }
  .band {
    position: absolute; bottom: 0; height: 22px;
  }
  .band-green { left: 0; width: 61%; background: var(--brand-green); }
  .band-blue { left: 62.2%; right: 0; background: var(--brand-blue); }
  /* Back */
  .card-back {
    background: linear-gradient(135deg, #262626 0%, var(--card-black) 55%, #323232 100%);
    display: flex; align-items: center; justify-content: center; gap: 30px;
  }
  .card-back .brand-mark { width: 130px; height: 130px; background: var(--brand-blue); }
  .card-back .brand-name { font-size: 40px; color: var(--brand-blue); text-align: left; }
</style>
</head>
<body>
<main class="sheet">
  <section class="card card-front">
    <div class="identity">
      <h1 class="name">MARCUS HALE</h1>
      <p class="role">CEO | FOUNDER</p>
    </div>
    <ul class="contacts">
      <li>
        <svg viewBox="0 0 24 24" aria-hidden="true"><path fill="#0f9470" d="M6.6 10.8a15.1 15.1 0 0 0 6.6 6.6l2.2-2.2a1 1 0 0 1 1-.25 11.4 11.4 0 0 0 3.6.57 1 1 0 0 1 1 1V20a1 1 0 0 1-1 1A17 17 0 0 1 3 4a1 1 0 0 1 1-1h3.5a1 1 0 0 1 1 1c0 1.25.2 2.45.57 3.57a1 1 0 0 1-.25 1z"/></svg>
        555-214-3860
      </li>
      <li>
        <svg viewBox="0 0 24 24" aria-hidden="true"><rect x="2" y="5" width="20" height="14" fill="#0f9470"/><path d="M2 5l10 8 10-8" fill="none" stroke="#fff" stroke-width="1.6"/></svg>
        hello@jadelineapparel.com
      </li>
      <li>
        <svg viewBox="0 0 24 24" aria-hidden="true"><g fill="none" stroke="#0f9470" stroke-width="2"><circle cx="12" cy="12" r="9.5"/><ellipse cx="12" cy="12" rx="4" ry="9.5"/><path d="M2.5 12h19M4 7h16M4 17h16"/></g></svg>
        www.jadelineapparel.com
      </li>
      <li>
        <span class="social-box" aria-hidden="true"></span>
        <span class="social-box" aria-hidden="true"></span>
        @jadelineapparel
      </li>
    </ul>
    <div class="brand-lockup">
      <span class="brand-mark" aria-hidden="true"></span>
      <p class="brand-name">JADELINE<br>APPAREL</p>
    </div>
    <span class="band band-green"></span>
    <span class="band band-blue"></span>
  </section>

  <section class="card card-back">
    <span class="brand-mark" aria-hidden="true"></span>
    <p class="brand-name">JADELINE<br>APPAREL</p>
  </section>
</main>
</body>
</html>
```